Glimmerseal pond linings website template

We need a template for our new website. Glimmerseal is currently marketed through www.tarpavale.com.au, and we are moving the pond/dam linings to a dedicated site www.glimmerseal.com.au

The site is essentially brochureware. The content (less landing page & photo gallery) is on the new site to give you a better idea of what we do. We are also on Facebook.com/glimmerseal

We are looking for a template/style which we can adapt to the different sections of the site as required. We also get a lot of phone/tablet visitors so an alternative mobile layout would be a bonus, but by no means required.

I am proficient in HTML/CSS & javascript so can code most designs thrown at me.

Any icons or interface fonts should be freely available web fonts where possible.

Target Market(s)

We are targeting both landscape professionals (design & construction) as well as the DIY market for ponds/wateragrdens.

Industry/Entity Type

Moving

Requirements
Must have
• We need a design (preferably layered PSD or AI) as basis for our overall site look and feel. Fonts/iconography/layout are where we are lacking. We can do the HTML/CSS/JS/PHP internally.
Nice to have
• A style guide either in file or separate would be nice.
Layers with effect (i.e.. :hover, CSS3 transition endpoints, etc)

```html
<!DOCTYPE html>
<html lang="en">
<head>
<meta charset="utf-8">
<title>Glimmerseal – Pond Liners</title>
<link rel="stylesheet" href="https://fonts.googleapis.com/css2?family=Mulish:wght@700;800&family=PT+Sans:wght@400;700&display=swap">
<style>
:root{
  --green:#6f9a2a;
  --green-dark:#5f8a22;
  --lime:#bccf2b;
  --navy:#0e3a78;
  --text:#6b6b6b;
  --rule:#e6e6e6;
  --white:#ffffff;
  --footer:#6e9a2d;
}
*{box-sizing:border-box;margin:0;padding:0}
html,body{width:1108px;height:1200px;overflow:hidden;background:var(--white)}
body{font-family:"PT Sans",Arial,sans-serif;color:var(--text);position:relative}
.wrap{position:absolute;left:110px;width:888px}

/* header */
.site-header{position:absolute;top:0;left:0;width:1108px;height:90px;border-bottom:1px solid var(--rule)}
.brand{position:absolute;left:110px;top:22px;display:flex;align-items:center;gap:10px}
.brand-mark{width:40px;height:40px;background:var(--green)}
.brand-name{font-family:"Mulish",sans-serif;font-weight:800;font-size:28px;color:var(--green);letter-spacing:.5px}
.search{position:absolute;left:766px;top:27px;width:209px;height:28px;border-radius:14px;
  background:linear-gradient(#e4e4e4,#f3f3f3);border:1px solid #d4d4d4;box-shadow:inset 0 1px 3px rgba(0,0,0,.15)}
.search svg{position:absolute;right:12px;top:7px}

/* nav */
.main-nav{position:absolute;top:90px;left:0;width:1108px;height:39px}
.main-nav ul{list-style:none;display:flex;justify-content:space-between;position:absolute;left:129px;width:848px;top:12px}
.main-nav a{font-family:"Mulish",sans-serif;font-weight:800;font-size:12px;color:var(--green);text-decoration:none;letter-spacing:.3px}

/* hero */
.hero{position:absolute;top:129px;left:0;width:1108px;height:388px;
  background:linear-gradient(160deg,#4f6b2c 0%,#8a8a80 30%,#6f7a5e 45%,#3f6f1a 65%,#2f5c12 100%)}
.hero-dots{position:absolute;top:360px;left:548px;display:flex;gap:6px}
.hero-dots span{width:13px;height:13px;border-radius:50%;background:#3d3d3d;box-shadow:inset 0 1px 2px rgba(0,0,0,.6)}
.hero-dots span.active{background:#f2a20c}

/* headings */
.section-title{font-family:"Mulish",sans-serif;font-weight:800;font-size:21px;color:var(--green)}
.section-title em{font-style:normal;color:var(--lime)}

/* buttons */
.btn{display:inline-block;height:28px;line-height:28px;padding:0 8px;font-family:"Mulish",sans-serif;
  font-weight:800;font-size:10px;color:var(--white);background:var(--green);text-decoration:none;letter-spacing:.2px}
.btn.navy{background:var(--navy)}

/* welcome */
.welcome{position:absolute;left:110px;top:534px;width:584px}
.welcome-photo{position:absolute;left:0;top:43px;width:278px;height:185px;
  background:linear-gradient(170deg,#7f8a82,#4d5a5e 55%,#8b9799)}
.welcome-text{position:absolute;left:285px;top:41px;width:299px;text-align:justify}
.lead{font-size:13px;line-height:16.6px;color:var(--green)}
.body-copy{font-size:10.5px;line-height:15.7px;color:var(--text);margin-top:15px}
.welcome .btn{position:absolute;left:-1px;top:245px}

/* happenings */
.happenings{position:absolute;left:719px;top:534px;width:278px}
.news-photo{position:absolute;left:0;top:43px;width:278px;height:111px;
  background:linear-gradient(160deg,#8fa36a,#6d8a3a 50%,#a9b86a)}
.news-title{position:absolute;top:164px;font-size:13px;color:var(--green)}
.news-text{position:absolute;top:181px;width:278px;font-size:10.5px;line-height:16.5px;text-align:justify}
.happenings .btn{position:absolute;left:0;top:245px}

/* liner styles */
.liners{position:absolute;left:110px;top:851px;width:888px;display:flex;gap:24px}
.liner{width:204px}
.liner-title{font-family:"Mulish",sans-serif;font-weight:800;font-size:17px;color:var(--navy);height:38px}
.liner-photo{width:204px;height:111px}
.p1{background:linear-gradient(180deg,#7ea444,#3d95b8 55%,#2f7fa3)}
.p2{background:linear-gradient(180deg,#8aa84a,#a09c8f 50%,#6a6f70)}
.p3{background:linear-gradient(180deg,#5b7d35,#6c8a3a 50%,#86b73d)}
.p4{background:linear-gradient(180deg,#6a6450,#7a8a4a 50%,#6b8a3a)}
.liner p{font-size:10.5px;line-height:14.8px;text-align:justify;margin:10px 0 9px}

/* footer */
.site-footer{position:absolute;left:0;top:1135px;width:1108px;height:65px;background:var(--footer)}
.copyright{position:absolute;left:109px;top:26px;font-family:Arial,sans-serif;font-size:11px;color:var(--white)}
.social{position:absolute;left:840px;top:22px;display:flex;gap:6px;list-style:none}
.social li{width:26px;height:26px;background:rgba(255,255,255,.22);border:1px solid rgba(255,255,255,.4)}
</style>
</head>
<body>

<header class="site-header">
  <div class="brand"><span class="brand-mark"></span><span class="brand-name">Glimmerseal</span></div>
  <div class="search" role="search">
    <svg width="12" height="12" viewBox="0 0 12 12"><circle cx="4.5" cy="4.5" r="3.2" fill="none" stroke="#c4c4c4" stroke-width="1.6"/><line x1="7" y1="7" x2="11" y2="11" stroke="#c4c4c4" stroke-width="2"/></svg>
  </div>
</header>

<nav class="main-nav">
  <ul>
    <li><a href="#">HOME</a></li>
    <li><a href="#">ABOUT US</a></li>
    <li><a href="#">HAPPENINGS</a></li>
    <li><a href="#">GALLERY</a></li>
    <li><a href="#">LINER STYLES</a></li>
    <li><a href="#">PREPARATION</a></li>
    <li><a href="#">INSTALLATION</a></li>
    <li><a href="#">CONTACT US</a></li>
  </ul>
</nav>

<section class="hero" role="img" aria-label="Garden pond with large stepping stones crossing still green water, ferns and trees around">
  <div class="hero-dots"><span class="active"></span><span></span><span></span></div>
</section>

<section class="welcome">
  <h2 class="section-title">Welcome to <em>Glimmerseal!</em></h2>
  <div class="welcome-photo" role="img" aria-label="Stream of water cascading over rounded river rocks beside a timber fence"></div>
  <div class="welcome-text">
    <p class="lead">Glimmerseal has been manufactured, marketed and installed throughout Australia and the Pacific Rim since the early 1980’s for a variety of domestic and commercial applications.</p>
    <p class="body-copy">Glimmerseal pond liners put an end to the complicated and time consuming installation used by other methods. Simply excavate or construct the desired shape of your pond pool or water garden, indoor or outdoor, place your Glimmerseal into position and secure the edges. It can easily be completed in a weekend. Glimmerseal pond liners are long lasting, economical to install and completely maintenance free.</p>
  </div>
  <a class="btn" href="#">READ MORE</a>
</section>

<section class="happenings">
  <h2 class="section-title">Happenings</h2>
  <div class="news-photo" role="img" aria-label="Show garden with tall trees, ferns and a rust-coloured pavilion"></div>
  <h3 class="news-title">Harrowmere 2013 – Best In Show</h3>
  <p class="news-text">The 2013 Australian entry to the Harrowmere Garden Show, was designed and built by award winning designer Dorian Wexley.</p>
  <a class="btn" href="#">READ MORE</a>
</section>

<section class="liners">
  <article class="liner">
    <h3 class="liner-title">Flat Sheet Liners</h3>
    <div class="liner-photo p1" role="img" aria-label="Blue pond edged with rocks and tropical plants"></div>
    <p>A flat sheet liner is the most common liner we manufacture and is suitable for most pond designs.</p>
    <a class="btn navy" href="#">READ MORE</a>
  </article>
  <article class="liner">
    <h3 class="liner-title">Composite Liners</h3>
    <div class="liner-photo p2" role="img" aria-label="Tiered rock waterfall flowing into a pond on a lawn"></div>
    <p>A flat sheet liner is the most common liner we manufacture and is suitable for most pond designs.</p>
    <a class="btn navy" href="#">READ MORE</a>
  </article>
  <article class="liner">
    <h3 class="liner-title">Profile Liners</h3>
    <div class="liner-photo p3" role="img" aria-label="Lily pond in a lush lawn garden with white stone edging"></div>
    <p>A flat sheet liner is the most common liner we manufacture and is suitable for most pond designs.</p>
    <a class="btn navy" href="#">READ MORE</a>
  </article>
  <article class="liner">
    <h3 class="liner-title">Special Project Liners</h3>
    <div class="liner-photo p4" role="img" aria-label="Rocky stream with water lilies beside a cabin and garden"></div>
    <p>A flat sheet liner is the most common liner we manufacture and is suitable for most pond designs.</p>
    <a class="btn navy" href="#">READ MORE</a>
  </article>
</section>

<footer class="site-footer">
  <p class="copyright">© 2013 Glimmerseal | All Rights Reserved.</p>
  <ul class="social" aria-label="Social links">
    <li aria-label="Social link"></li>
    <li aria-label="Social link"></li>
    <li aria-label="News feed"></li>
    <li aria-label="Video channel"></li>
    <li aria-label="Social link"></li>
  </ul>
</footer>

</body>
</html>
```